Cybersecurity company is looking for business card.

I need a business card design for our company, we are a cybersecurity company providing advance technology to protect agains any kind of malware. We need a fresh modern design it should communicate modern, technology and growth.

Target Market(s)

Business to business

Industry/Entity Type

Business

Contact Information for Business Card

Should have location, address, fax, mobile, phone, email and website.

Requirements
Must have
• Must follow company's logo color and style. Must have the company's log on its.

```html
<!DOCTYPE html>
<html lang="en">
<head>
<meta charset="utf-8">
<title>Vantrix Business Card</title>
<link href="https://fonts.googleapis.com/css2?family=Arimo:wght@400;700&family=Archivo+Black&display=swap" rel="stylesheet">
<style>
  :root {
    --backdrop: #d9d9d9;
    --card: #f7f7f5;
    --grid-line: #c9c9c9;
    --ink-dark: #1c1c1c;
    --ink-logo-front: #5a5a5a;
    --accent-red: #9c1a1a;
    --accent-mark: #e0785e;
  }
  * { margin: 0; padding: 0; box-sizing: border-box; }
  html, body {
    width: 1200px;
    height: 800px;
    overflow: hidden;
    background: var(--backdrop);
    font-family: "Arimo", Arial, sans-serif;
  }
  .stage {
    width: 1200px;
    height: 800px;
    display: flex;
    align-items: center;
    justify-content: center;
    gap: 40px;
  }
  .card {
    width: 540px;
    height: 309px;
    background: var(--card);
    position: relative;
    box-shadow: 0 2px 6px rgba(0,0,0,0.15);
    overflow: hidden;
  }
  /* Front side */
  .card--front {
    display: flex;
    align-items: center;
    justify-content: center;
  }
  .brand {
    display: flex;
    align-items: flex-start;
    gap: 6px;
    font-family: "Arimo", Arial, sans-serif;
    font-weight: 700;
    letter-spacing: -1px;
    line-height: 1;
  }
  .brand__mark {
    width: 12px;
    height: 12px;
    background: var(--accent-mark);
    margin-top: 6px;
  }
  .card--front .brand__name {
    font-size: 104px;
    color: var(--ink-logo-front);
  }
  .card--front .brand__mark {
    width: 18px;
    height: 18px;
    margin-top: 8px;
  }
  /* Back side */
  .card--back {
    background-color: var(--card);
    background-image:
      linear-gradient(var(--grid-line) 1px, transparent 1px),
      linear-gradient(90deg, var(--grid-line) 1px, transparent 1px);
    background-size: 27px 27px;
    background-position: -1px -1px;
  }
  .back__logo {
    position: absolute;
    top: 38px;
    right: 70px;
    text-align: right;
  }
  .card--back .brand__name {
    font-size: 58px;
    color: var(--ink-dark);
  }
  .back__location {
    font-size: 14px;
    letter-spacing: 4px;
    color: var(--ink-dark);
    margin-top: 2px;
    text-transform: uppercase;
  }
  .back__address {
    position: absolute;
    top: 128px;
    left: 20px;
    font-family: "Archivo Black", "Arial Black", sans-serif;
    font-size: 15.5px;
    color: var(--accent-red);
    line-height: 1;
  }
  .back__contacts {
    position: absolute;
    top: 148px;
    left: 20px;
    list-style: none;
    font-size: 12.5px;
    color: var(--ink-dark);
    line-height: 16px;
  }
  .back__web {
    position: absolute;
    bottom: 26px;
    left: 0;
    right: 0;
    text-align: center;
    font-size: 13px;
    color: var(--ink-dark);
    line-height: 20px;
  }
</style>
</head>
<body>
  <main class="stage">
    <section class="card card--front" aria-label="Card front">
      <div class="brand">
        <span class="brand__name">vantrix</span>
        <span class="brand__mark" aria-hidden="true"></span>
      </div>
    </section>

    <section class="card card--back" aria-label="Card back">
      <div class="back__logo">
        <div class="brand">
          <span class="brand__name">vantrix</span>
          <span class="brand__mark" aria-hidden="true"></span>
        </div>
        <p class="back__location">Harbor - Coastland</p>
      </div>
      <p class="back__address">Harbor Tech Park (HTP) -Meridian Avenue Road</p>
      <ul class="back__contacts">
        <li>Mobile: +970 55 123 XXXX</li>
        <li>Phone: 07 123 XXXX</li>
        <li>Fax: 07 123 XXXX</li>
        <li>E-mail : name.surname@vantrix.com</li>
      </ul>
      <div class="back__web">
        <p>name.surname@vantrix.com</p>
        <p>www.vantrix.com</p>
      </div>
    </section>
  </main>
</body>
</html>
```